New Year's card HTML

can you produce a best new years wishes 2018 design in HTML for our website as what I would like to send by email towards my network of candidates / customers ...

It must be wow, inspiring , design, meaningfull... MMM those people care about me, or those people will help me to go the extra mile, to help me to achieve my career goals, Your best move, enhance my possibilities, bring the love back

Target Market(s)

CEo's / CMO's/ HRDirectors network of 450k

Coding

Coded - Design and coding required

Number of Pages Required

1 page

Colors

Designer to choose colors to be used in the design.

Requirements
Must have
• Logo / visual / website adress www.dorimvale.com and a call to action
Should not have
• no sound as our business is confidential

```html
<!DOCTYPE html>
<html lang="en">
<head>
<meta charset="utf-8">
<title>Happy New Year 2018 – Dorimvale</title>
<link rel="stylesheet" href="https://fonts.googleapis.com/css2?family=Courgette&family=Cinzel:wght@500&family=Roboto:wght@700&display=swap">
<style>
  :root {
    --bg: #ffffff;
    --balloon-deep: #2f6fd0;
    --balloon-mid: #6fa2e6;
    --balloon-light: #dfe9f6;
    --gold: #f3d58a;
    --gold-deep: #c99a3a;
    --ink: #2b2118;
    --brand: #3d3d3d;
    --rule: #b9b9b9;
    --cta: #f0a019;
    --spark: #eed9a4;
    --glass: #d9c48a;
  }
  * { margin: 0; padding: 0; box-sizing: border-box; }
  html, body { width: 1200px; height: 720px; overflow: hidden; background: var(--bg); }
  .card { position: relative; width: 1200px; height: 720px; overflow: hidden; background: var(--bg); }
  .balloon-canopy, .fireworks, .champagne { position: absolute; }
  .balloon-canopy { left: 0; top: 0; width: 1200px; height: 720px; }
  .fireworks {
    left: 380px; top: 220px; width: 440px; height: 320px; border-radius: 50%;
    background: radial-gradient(ellipse at center, rgba(238,217,164,0.55) 0%, rgba(238,217,164,0.2) 45%, rgba(238,217,164,0) 70%);
  }
  .champagne {
    left: 986px; top: 512px; width: 190px; height: 196px; border-radius: 40px 40px 8px 8px;
    background: linear-gradient(180deg, #f4ecd2 0%, var(--glass) 60%, #efe6cc 100%);
  }
  .greeting {
    position: absolute; left: 0; width: 1200px; text-align: center;
    font-family: "Courgette", cursive; color: var(--gold);
    -webkit-text-stroke: 2px var(--ink);
    text-shadow: 3px 4px 0 rgba(43,33,24,0.35);
  }
  .greeting-line { top: 296px; font-size: 62px; line-height: 1; }
  .greeting-year { top: 392px; font-size: 110px; line-height: 1; color: #f7e3a6; }
  .signoff {
    position: absolute; left: 420px; top: 548px; width: 360px; height: 20px;
    display: flex; align-items: center; gap: 14px;
  }
  .signoff::before, .signoff::after { content: ""; flex: 1; height: 1px; background: var(--rule); }
  .signoff-by { font-family: "Courgette", cursive; font-size: 18px; color: var(--cta); }
  .brand {
    position: absolute; left: 0; top: 578px; width: 1200px;
    display: flex; justify-content: center; align-items: center; gap: 20px;
  }
  .brand-mark { width: 34px; height: 34px; background: var(--brand); }
  .brand-name { font-family: "Cinzel", serif; font-weight: 500; font-size: 48px; letter-spacing: 2px; color: var(--brand); }
  .cta {
    position: absolute; left: 0; top: 644px; width: 1200px; text-align: center;
  }
  .cta a {
    font-family: "Roboto", sans-serif; font-weight: 700; font-size: 25px; color: var(--cta);
    text-decoration: none; border-bottom: 1.5px solid var(--cta); padding-bottom: 2px;
  }
</style>
</head>
<body>
<main class="card">
  <svg class="balloon-canopy" viewBox="0 0 1200 720" role="img" aria-label="Canopy of blue and white balloons with curling ribbons hanging from above">
    <defs>
      <linearGradient id="canopyTone" x1="0" y1="0" x2="1" y2="1">
        <stop offset="0" stop-color="var(--balloon-mid)"/>
        <stop offset="0.35" stop-color="var(--balloon-deep)"/>
        <stop offset="0.65" stop-color="var(--balloon-light)"/>
        <stop offset="1" stop-color="var(--balloon-mid)"/>
      </linearGradient>
    </defs>
    <path fill="url(#canopyTone)" d="M0 0 H1200 V470 C1170 500 1110 520 1060 500 C1010 430 990 330 930 270 C850 200 760 190 690 210 C640 225 610 235 600 240 C560 225 480 200 400 210 C320 225 260 280 230 360 C200 440 150 520 90 560 C60 580 20 590 0 590 Z"/>
  </svg>
  <div class="fireworks" role="img" aria-label="Soft golden firework bursts behind the greeting"></div>

  <h1 class="greeting greeting-line">Happy New Year</h1>
  <p class="greeting greeting-year">2018</p>

  <div class="signoff"><span class="signoff-by">By</span></div>
  <div class="brand">
    <span class="brand-mark"></span>
    <span class="brand-name">DORIMVALE</span>
  </div>
  <p class="cta"><a href="https://www.dorimvale.com">Visit Dorimvale&nbsp;&nbsp;»</a></p>

  <div class="champagne" role="img" aria-label="Two champagne flutes with golden curling ribbon"></div>
</main>
</body>
</html>
```